Financial Workshop for Halvorsen Financial

Postcard to comply with PRLQ. Invitation to workshop for 55+ senior community.
"Estate Conservation Strategies and Legacy Planning"
Building a sound and lasting retirement portfolio with a focus on growth and asset protection.
Developing investment objectives
Understanding risk adversity
Preserving assets
Conservative growth strategies for saving and investing
Planning for uncovered health care costs
Estate planning
Reid Halvorsen, Certified Financial Plannerâ„¢

add to the text (bullets) after Estate Planning (on same line) and Wealth Transfer Strategies Thank you Added Friday, October 13, 2017

Target Market(s)

Seniors

Industry/Entity Type

Financial

Font styles to use
Sans Serif

Colors

Designer to choose colors to be used in the design.

Requirements
Must have
• Logo
• Eye-catching images
• Easy to read geared for seniors
• Upscale professional look
• Afresh new look from previous samples sent.
Nice to have
• Something that stands out among the many postcard mail pieces they will get.
Should not have
• aside from logo/photo samples are an example of previous workshops and should not be reused.

```html
<!DOCTYPE html>
<html lang="en">
<head>
<meta charset="utf-8">
<title>Halvorsen Financial – Workshop Postcard</title>
<link rel="stylesheet" href="https://fonts.googleapis.com/css2?family=Open+Sans:ital,wght@0,400;0,600;0,700;1,400;1,600&family=Roboto+Condensed:wght@700&family=Montserrat:wght@800&display=swap">
<style>
:root{
  --bg:#9cb0c4;
  --navy:#1e2b8f;
  --navy-deep:#17206e;
  --royal:#1f3fa6;
  --slate:#7d8a99;
  --slate-dark:#5f6b79;
  --sky:#cfe6f7;
  --sky-deep:#a9d2ef;
  --ink:#2b3340;
  --white:#ffffff;
}
*{box-sizing:border-box;margin:0;padding:0}
html,body{width:1200px;height:696px;overflow:hidden}
body{background:var(--bg);font-family:"Open Sans",sans-serif;color:var(--ink);position:relative}
.card{position:absolute;top:170px;width:570px;height:356px;overflow:hidden;border:3px solid var(--white);box-shadow:0 6px 18px rgba(0,0,0,.25)}
/* ---------- mailing side ---------- */
.mailer{left:20px;background:linear-gradient(20deg,var(--sky-deep) 0%,#e6f2fb 45%,var(--white) 70%)}
.headshot{position:absolute;left:22px;top:16px;width:92px;height:92px;border-radius:50%;background:linear-gradient(180deg,#8c97a5,#4f5a68);border:3px solid #9aa6b3}
.advisor-name{position:absolute;left:130px;top:32px;font-family:"Montserrat",sans-serif;font-weight:800;font-size:24px;color:var(--navy)}
.advisor-title{position:absolute;left:128px;top:64px;font-style:italic;font-size:11.5px;color:var(--navy);letter-spacing:.3px}
.bio{position:absolute;left:20px;top:116px;width:300px;font-style:italic;font-weight:600;font-size:8.6px;line-height:15px;text-align:justify}
.topics-tab{position:absolute;left:0;top:204px;width:170px;height:24px;background:var(--slate);border-radius:0 8px 8px 0;color:var(--white);font-weight:700;font-style:italic;font-size:12px;letter-spacing:1.4px;padding:4px 0 0 18px}
.topics{position:absolute;left:24px;top:238px;list-style:none;font-style:italic;font-weight:600;font-size:10px;line-height:18px}
.topics li::before,.perks li::before,.lead::before{content:"";display:inline-block;width:7px;height:7px;border-radius:50%;background:radial-gradient(circle at 35% 35%,#cdd3da,#5f6b79);margin-right:8px;vertical-align:1px}
.indicia{position:absolute;right:14px;top:18px;width:66px;height:56px;border:1.5px solid var(--slate-dark);font-size:7px;line-height:9px;text-align:center;padding-top:5px;color:var(--ink)}
.address-lines{position:absolute;right:22px;top:150px;width:190px}
.address-lines span{display:block;height:1px;background:var(--slate);margin-bottom:26px}
.contact{position:absolute;right:20px;top:262px;width:165px;font-size:9px;line-height:16px;font-style:normal}
.contact b{color:var(--navy)}
.email-bar{position:absolute;right:0;bottom:14px;width:200px;height:26px;background:var(--slate);border-radius:13px 0 0 13px;color:var(--white);font-size:10px;font-weight:600;padding:5px 0 0 20px}
/* ---------- offer side ---------- */
.offer{left:610px;background:linear-gradient(180deg,var(--white) 55%,var(--sky) 100%)}
.photo{position:absolute;left:0;top:0;width:100%;height:170px;background:linear-gradient(90deg,#b9a58d 0%,#d8d2c6 35%,#e9e4dc 55%,#c9b6a6 75%,#eceff2 100%)}
.brand{position:absolute;left:22px;top:14px;display:flex;align-items:center;gap:8px;color:var(--navy);font-weight:600;font-size:20px;letter-spacing:4px;line-height:22px;background:rgba(255,255,255,.85);padding:6px 10px}
.brand i{width:22px;height:22px;background:var(--navy)}
.invite{position:absolute;left:36px;top:82px;color:var(--white);font-weight:700;font-size:15px;line-height:22px;text-shadow:0 1px 3px rgba(0,0,0,.5)}
.swoosh{position:absolute;left:0;top:118px}
.headline{position:absolute;left:0;top:196px;width:100%;text-align:center;font-family:"Roboto Condensed",sans-serif;font-weight:700;font-size:16px;color:var(--navy-deep)}
.lead{position:absolute;left:22px;top:224px;font-weight:600;font-size:9px;white-space:nowrap}
.perks{position:absolute;list-style:none;font-weight:600;font-size:9px;line-height:22px;white-space:nowrap}
.perks.left{left:22px;top:242px}
.perks.right{left:262px;top:250px}
.signature{position:absolute;left:150px;bottom:0;width:270px;height:26px;background:var(--slate);border-radius:12px 12px 0 0;color:var(--white);font-variant:small-caps;font-size:13px;text-align:center;padding-top:3px;letter-spacing:.5px}
</style>
</head>
<body>

<section class="card mailer">
  <div class="headshot" role="img" aria-label="Portrait photo of the advisor"></div>
  <h1 class="advisor-name">Reid Halvorsen</h1>
  <p class="advisor-title">CERTIFIED FINANCIAL PLANNER™</p>
  <p class="bio">Reid Halvorsen is a CERTIFIED FINANCIAL PLANNER™, specializing in asset management of IRA, retirement and investment accounts. Halvorsen Advisors, LLC is an independent Registered Investment Advisor with a low cost, commission free business model. Concierge level service is provided to Willow Bend residents.</p>
  <div class="indicia">PRSRT STD<br>ECRWSS<br>U.S.POSTAGE<br>PAID<br>PRLQ</div>
  <div class="address-lines"><span></span><span></span><span></span><span></span></div>
  <div class="topics-tab">Workshop Topics:</div>
  <ul class="topics">
    <li>How hidden costs drag down investment results</li>
    <li>Maximizing income flow in Retirement</li>
    <li>Growing and Protecting Retirement Assets</li>
    <li>Estate Conservation Strategies</li>
  </ul>
  <address class="contact">
    <b>A:</b> 418 Maple Ridge Lane,<br>Raleigh, NC 27609<br>
    <b>P:</b> 919-555-0142 | <b>F:</b> (919) 555-0187
  </address>
  <div class="email-bar">reid@halvorsenfinancial.com</div>
</section>

<section class="card offer">
  <div class="photo" role="img" aria-label="Photo of a smiling senior couple reading together at home"></div>
  <div class="brand"><i></i><span>HALVORSEN<br>FINANCIAL</span></div>
  <p class="invite">Invitation to workshop<br>for 55+ senior community.</p>
  <svg class="swoosh" width="570" height="80" viewBox="0 0 570 80" aria-hidden="true">
    <path d="M0 80 C140 10 400 0 570 50 L570 80 Z" fill="#ffffff"/>
    <path d="M0 62 C150 0 380 -6 570 40 L570 58 C390 14 160 22 0 72 Z" fill="#7d8a99"/>
    <path d="M120 40 C260 8 420 12 570 56 L570 68 C420 26 270 26 120 40 Z" fill="#1f3fa6"/>
  </svg>
  <h2 class="headline">Estate Conservation Strategies and Legacy Planning</h2>
  <p class="lead">Building a sound and lasting retirement portfolio with a focus on growth and asset protection.</p>
  <ul class="perks left">
    <li>Developing investment objectives</li>
    <li>Preserving assets</li>
    <li>Planning for uncovered health care costs</li>
  </ul>
  <ul class="perks right">
    <li>Understanding risk adversity</li>
    <li>Conservative growth strategies for saving and investing</li>
    <li>Estate planning and Wealth Transfer Strategies</li>
  </ul>
  <div class="signature">Reid Halvorsen, Certified Financial Planner™</div>
</section>

</body>
</html>
```